SPARK - and the compass of quiet days

I´m writing a book about CHANGE and the skills leaders needs to embody the transformation from being amanager to become leaders.
The title of the book in Icelandic is the same as the name of the project (which I want to be used on the designes is:) HAFALDAN
(with the subtitle:) og listin að hlusta

Change is not controlled or managed – Leading effective change is an art form which is one of the big reasons for why 70% of changes within companies fail. The main reason however, is that managers are tasked with managing and directing them. The art form of change is to put it in the hands of leaders who possess the emotional intelligence that is needed – all their other advantages intact – to lead change all the way.

The big problem when it comes to change is that there are too many managers and too few leaders within companies – leaders who possess emotional intelligence which is the most important skill a leader embodies to empower change. A leader has what it takes to empower followership.

A manager tends to push and control, make decisions that he presupposes others to implement the way he expects. An emotionally competent leader leads by example and enhances followership on that journey because of the trust and respect he has earned.

In few words: SOFT SKILLS ARE THE NEW HARD SKILLS!

```html
<!DOCTYPE html>
<html lang="is">
<head>
<meta charset="utf-8">
<title>HAFALDAN – og listin að hlusta</title>
<link rel="stylesheet" href="https://fonts.googleapis.com/css2?family=Bebas+Neue&family=Lato:wght@400&display=swap">
<style>
  :root {
    --stage: #3b3b3b;
    --cover-dark: #0c0c0c;
    --cover-mid: #232323;
    --band-red: #b81414;
    --band-deep: #7e0707;
    --torn-white: #e4e4e2;
    --title-white: #ffffff;
    --author-red: #7c1212;
  }
  html, body {
    margin: 0;
    width: 1200px;
    height: 1200px;
    overflow: hidden;
    background: var(--stage);
  }
  .book-cover {
    position: absolute;
    left: 240px;
    top: 60px;
    width: 720px;
    height: 1080px;
    background: radial-gradient(ellipse at 50% 45%, var(--cover-mid) 0%, var(--cover-dark) 75%);
    overflow: hidden;
  }
  .torn-band {
    position: absolute;
    inset: 0;
    width: 720px;
    height: 1080px;
  }
  .cover-title {
    position: absolute;
    left: 0;
    right: 0;
    top: 405px;
    margin: 0;
    text-align: center;
    font-family: "Bebas Neue", "Oswald", sans-serif;
    font-weight: 400;
    font-size: 205px;
    line-height: 1;
    letter-spacing: 2px;
    color: var(--title-white);
  }
  .cover-subtitle {
    position: absolute;
    left: 0;
    right: 0;
    top: 628px;
    margin: 0;
    text-align: center;
    font-family: "Lato", sans-serif;
    font-size: 34px;
    color: var(--title-white);
    text-transform: capitalize;
  }
  .cover-author {
    position: absolute;
    left: 0;
    right: 0;
    top: 940px;
    margin: 0;
    text-align: center;
    font-family: "Lato", sans-serif;
    font-size: 42px;
    letter-spacing: 1px;
    color: var(--author-red);
  }
</style>
</head>
<body>
  <main class="book-cover">
    <svg class="torn-band" viewBox="0 0 720 1080" aria-hidden="true">
      <defs>
        <radialGradient id="band-fill" cx="50%" cy="50%" r="70%">
          <stop offset="0%" stop-color="var(--band-red)"/>
          <stop offset="100%" stop-color="var(--band-deep)"/>
        </radialGradient>
      </defs>
      <polygon class="torn-edge-top" fill="var(--torn-white)"
        points="0,298 40,292 80,300 120,289 160,296 200,302 240,291 280,297 320,288 360,299 400,294 440,301 480,290 520,296 560,303 600,293 640,298 680,290 720,295 720,330 0,330"/>
      <polygon class="torn-edge-bottom" fill="var(--torn-white)"
        points="0,730 720,730 720,760 680,748 640,757 600,752 560,763 520,749 480,753 440,761 400,747 360,758 320,750 280,764 240,751 200,762 160,748 120,755 80,760 40,752 0,756"/>
      <polygon class="band-red" fill="url(#band-fill)"
        points="0,312 40,318 80,308 120,320 160,314 200,309 240,322 280,311 320,316 360,306 400,319 440,313 480,310 520,321 560,312 600,317 640,307 680,315 720,318 720,747 680,734 640,743 600,738 560,749 520,735 480,741 440,746 400,731 360,744 320,737 280,750 240,739 200,745 160,733 120,740 80,748 40,736 0,742"/>
    </svg>
    <h1 class="cover-title">HAFALDAN</h1>
    <p class="cover-subtitle">og listin að hlusta</p>
    <p class="cover-author">AUTHOR NAME</p>
  </main>
</body>
</html>
```